Revamp of business card

i need to revamp my business card to look more modern and neat

Contact Information for Business Card

details provided in pdf file, text will change

```html
<!DOCTYPE html>
<html lang="en">
<head>
<meta charset="utf-8">
<title>Inkbloom Business Card</title>
<link rel="stylesheet" href="https://fonts.googleapis.com/css2?family=Nunito:wght@400;600;700;800&display=swap">
<style>
  :root {
    --bg: #7a7a7a;
    --card: #ffffff;
    --brand-orange: #ef4e23;
    --brand-green: #1f9448;
    --text-grey: #4a4a4a;
    --bar-orange: #f7941d;
    --bar-green: #1f9448;
    --bar-blue: #124b94;
    --bar-red: #ec1c24;
  }
  * { box-sizing: border-box; margin: 0; padding: 0; }
  html, body { width: 1200px; height: 1200px; overflow: hidden; }
  body {
    background: var(--bg);
    font-family: "Nunito", sans-serif;
    position: relative;
  }
  .card {
    position: absolute;
    left: 262px;
    width: 686px;
    height: 392px;
    background: var(--card);
    overflow: hidden;
  }
  .card--front { top: 166px; }
  .card--back { top: 653px; }

  .edge-bars {
    position: absolute;
    top: 0;
    width: 10px;
    height: 100%;
    display: flex;
    flex-direction: column;
    gap: 4px;
  }
  .card--front .edge-bars { right: 0; }
  .card--back .edge-bars { left: 0; }
  .edge-bars span { flex: 1; }
  .edge-bars .orange { background: var(--bar-orange); }
  .edge-bars .green { background: var(--bar-green); }
  .edge-bars .blue { background: var(--bar-blue); }
  .edge-bars .red { background: var(--bar-red); }

  /* Front */
  .brand {
    position: absolute;
    left: 43px;
    top: 48px;
  }
  .brand-name {
    font-size: 66px;
    font-weight: 800;
    color: var(--brand-orange);
    line-height: 1;
    letter-spacing: -1px;
  }
  .brand-tagline {
    font-size: 12.5px;
    color: var(--text-grey);
    text-align: right;
    margin-top: 4px;
  }
  .person { position: absolute; left: 43px; top: 155px; }
  .person-name {
    font-size: 23px;
    font-weight: 700;
    color: var(--brand-orange);
  }
  .person-title {
    font-size: 15px;
    color: var(--brand-green);
    margin-top: 1px;
  }
  .address {
    position: absolute;
    left: 43px;
    top: 215px;
    font-size: 15px;
    line-height: 19.5px;
    color: var(--text-grey);
  }
  .contacts {
    position: absolute;
    left: 43px;
    top: 281px;
    list-style: none;
    font-size: 15px;
    line-height: 19.7px;
    color: var(--text-grey);
  }
  .contacts li { display: flex; align-items: center; gap: 8px; }
  .contacts svg { width: 13px; height: 13px; fill: var(--brand-orange); flex: none; }

  /* Back */
  .services { position: absolute; left: 37px; top: 30px; }
  .service { margin-bottom: 8px; }
  .service h2 {
    font-size: 20px;
    font-weight: 700;
    color: var(--brand-orange);
    line-height: 1.25;
  }
  .service p {
    font-size: 15px;
    font-weight: 600;
    color: var(--text-grey);
    line-height: 19px;
  }
  .service .links {
    font-weight: 400;
    font-size: 14.5px;
  }
  .socials {
    position: absolute;
    left: 38px;
    top: 338px;
    display: flex;
    align-items: center;
    gap: 7px;
    font-size: 15px;
    font-weight: 600;
    color: var(--text-grey);
  }
  .social-dot {
    width: 18px; height: 18px; border-radius: 50%;
    background: var(--bar-blue);
  }
  .social-dot--alt { background: var(--brand-orange); margin-left: 8px; }
  .back-brand {
    position: absolute;
    left: 492px;
    top: 240px;
    display: flex;
    flex-direction: column;
    align-items: center;
    gap: 8px;
  }
  .back-brand-mark {
    width: 96px; height: 96px; border-radius: 50%;
    background: var(--brand-orange);
  }
  .back-brand-name {
    font-size: 30px;
    font-weight: 800;
    color: var(--brand-orange);
    line-height: 1;
  }
</style>
</head>
<body>

<section class="card card--front">
  <div class="brand">
    <div class="brand-name">Inkbloom</div>
    <div class="brand-tagline">where ink becomes art</div>
  </div>

  <div class="person">
    <div class="person-name">Darren Mehta</div>
    <div class="person-title">Diector</div>
  </div>

  <div class="address">
    G4, 18-24 Harbour Lane,<br>
    Wattle Court<br>
    Riverton, Riverton 5100
  </div>

  <ul class="contacts">
    <li>
      <svg viewBox="0 0 24 24"><path d="M6.6 10.8a15.1 15.1 0 0 0 6.6 6.6l2.2-2.2c.3-.3.7-.4 1-.2 1.1.4 2.3.6 3.6.6.6 0 1 .4 1 1V20c0 .6-.4 1-1 1A17 17 0 0 1 3 4c0-.6.4-1 1-1h3.5c.6 0 1 .4 1 1 0 1.3.2 2.5.6 3.6.1.3 0 .7-.2 1z"/></svg>
      0400 123 987
    </li>
    <li>
      <svg viewBox="0 0 24 24"><path d="M6.6 10.8a15.1 15.1 0 0 0 6.6 6.6l2.2-2.2c.3-.3.7-.4 1-.2 1.1.4 2.3.6 3.6.6.6 0 1 .4 1 1V20c0 .6-.4 1-1 1A17 17 0 0 1 3 4c0-.6.4-1 1-1h3.5c.6 0 1 .4 1 1 0 1.3.2 2.5.6 3.6.1.3 0 .7-.2 1z"/></svg>
      08 7000 1234
    </li>
    <li>
      <svg viewBox="0 0 24 24"><path d="M2 5h20v14H2z M2 5l10 8 10-8" fill="none" stroke="#ef4e23" stroke-width="2.4"/></svg>
      darren@inkbloom.com
    </li>
    <li>
      <svg viewBox="0 0 24 24"><circle cx="12" cy="12" r="10"/><path d="M2 12h20M12 2c3 3 3 17 0 20M12 2c-3 3-3 17 0 20" fill="none" stroke="#fff" stroke-width="1.6"/></svg>
      www.inkbloom.com.au
    </li>
  </ul>

  <div class="edge-bars">
    <span class="orange"></span><span class="green"></span><span class="blue"></span><span class="red"></span>
  </div>
</section>

<section class="card card--back">
  <div class="edge-bars">
    <span class="orange"></span><span class="green"></span><span class="blue"></span><span class="red"></span>
  </div>

  <div class="services">
    <div class="service">
      <h2>Tshirt prints &amp; Embroidery</h2>
      <p>Prints on all kinds of apparel and fabrics</p>
      <p class="links">www.threadly.com.au<br>www.plaincotton.com.au<br>www.stitchworks.com.au</p>
    </div>
    <div class="service">
      <h2>Prints on Promotional &amp; Giveaways</h2>
      <p>Mugs, Caps KeyChains,Name Tags,Wall Clocks ets</p>
    </div>
    <div class="service">
      <h2>Print &amp; Design Services</h2>
      <p>Business Cards, Flyers,<br>Brochures,Posters, Banners ets</p>
    </div>
    <div class="service">
      <h2>Photo Prints</h2>
      <p>HD&nbsp; Metal Prints to Photographic Paper Prints</p>
    </div>
  </div>

  <div class="socials">
    <span class="social-dot"></span><span>inkbloomstudio</span>
    <span class="social-dot social-dot--alt"></span><span>inkbloom</span>
  </div>

  <div class="back-brand">
    <div class="back-brand-mark"></div>
    <div class="back-brand-name">Inkbloom</div>
  </div>
</section>

</body>
</html>
```